Website Layout Design
Website layout design
Thanks for the PDF logo, it's vector and Illustrator-editable, so no need to get any other images.
I have a high res pdf image of the logo for use at http://lumavextra.com/press/logo.pdf
I am working on getting a high res graphic image as well
Dear project holder,
I am in....I am working on your project.thanks.
The only logo we have at the present time is the one on our website. You can feel free to download that from http://lumavextra.com I do not have the original adobe image. Please use the logo from the website for now and I will try to get a better one for you in the mean time
OK, header nav.
Still need the logo in high res or vector (if you have it w/o background, great!!!)
May you attached your company logo in a highest format? Thanks!
I prefer the Nav placement be in the header with drop down menus
the center section would be for me to place my content pages.
Hello!
I'm working on the project.
Question: in the Project Brief you indicated you "want in a webpage layout is a top header section with navigation and a bottom footer section", and in further description (at the bottom of the Brief) you indicated you want "Nav placement - left side"
So, which nav placement you like better? :)
Also, can you upload the logo in somewhat higher res (or vector even better)
Thanks!!!
-pbrandal

```html
<!DOCTYPE html>
<html lang="en">
<head>
<meta charset="utf-8">
<title>Lumavextra – Products to Maximize Life</title>
<link href="https://fonts.googleapis.com/css2?family=Lato:wght@400;700;900&family=Open+Sans:wght@400;600;700&display=swap" rel="stylesheet">
<style>
:root{
  --green-dark:#1f3d12;
  --green-mid:#2f5a1c;
  --green-leaf:#6b9b2c;
  --orange:#d9772c;
  --orange-light:#e98b3c;
  --white:#ffffff;
  --page:#f4f4f2;
  --text:#2b2b2b;
  --muted:#8a8a8a;
  --line:#d7d7d7;
}
*{box-sizing:border-box;margin:0;padding:0}
html,body{width:1200px;height:732px;overflow:hidden}
body{font-family:"Open Sans",Arial,sans-serif;color:var(--text);background:var(--page);position:relative}
.header{position:absolute;left:0;top:0;width:1200px;height:170px;background:linear-gradient(180deg,var(--green-dark),var(--green-mid) 70%,#3c6a24)}
.brand{position:absolute;left:140px;top:48px;display:flex;align-items:center;gap:12px}
.brand-mark{width:34px;height:34px;border-radius:50%;background:var(--green-leaf)}
.brand-name{font-family:"Lato",sans-serif;font-weight:900;font-size:44px;color:var(--orange-light);letter-spacing:1px}
.tagline{position:absolute;left:140px;top:128px;font-family:"Lato",sans-serif;font-size:12px;letter-spacing:2.6px;color:#9cc35a;font-weight:700}
.search{position:absolute;left:800px;top:38px;display:flex;height:38px}
.search-icon{width:42px;background:var(--orange);display:flex;align-items:center;justify-content:center}
.search-field{width:140px;background:var(--white);font-size:13px;font-style:italic;color:var(--muted);padding:10px}
.search-btn{width:76px;background:var(--orange);color:var(--white);font-size:14px;display:flex;align-items:center;justify-content:center}
.nav{position:absolute;left:475px;top:104px;width:648px;height:40px;background:var(--white);border-radius:4px;display:flex;align-items:center;padding:0 4px;font-size:15px}
.nav a{color:var(--text);text-decoration:none;padding:0 12px;border-right:1px solid var(--line);line-height:20px}
.nav a:last-child{border-right:0}
.nav a.active{background:var(--orange);color:var(--white);border-radius:3px;line-height:34px;padding:0 20px;border:0}
.box{position:absolute;left:139px;width:178px;background:var(--white);border:2px solid var(--orange)}
.box-title{background:var(--orange);color:var(--white);font-size:15px;padding:4px 8px;text-transform:none}
.videos{top:180px;height:163px}
.video-thumb{height:128px;background:linear-gradient(135deg,#cfd7d0,#8ea39a);display:flex;align-items:center;justify-content:center}
.categories{top:355px;height:113px}
.categories ul{list-style:none;padding:8px 10px;font-size:15px;line-height:22px}
.user{top:480px;height:180px}
.user-form{padding:10px 14px}
.field{height:26px;border:1px solid var(--line);border-radius:3px;margin-bottom:8px;font-size:13px;font-style:italic;color:var(--muted);text-align:center;line-height:24px}
.actions{display:flex;gap:14px;margin-top:4px}
.btn-small{background:var(--orange);color:var(--white);font-size:13px;border-radius:4px;padding:2px 12px}
.forgot{font-size:13px;font-style:italic;color:var(--muted);margin-top:8px;text-align:center}
.slider{position:absolute;left:326px;top:180px;width:735px;height:281px;border:2px solid var(--orange);border-radius:6px;background:linear-gradient(90deg,#ece6da,#f3efe6);overflow:hidden}
.slide-art{position:absolute;left:50px;top:40px;width:630px;height:160px;background:linear-gradient(90deg,#c9a23e,#8fae3c,#d06a2d,#6f9a34);opacity:.55;border-radius:30px}
.dots{position:absolute;left:50%;bottom:14px;transform:translateX(-50%);display:flex;gap:8px}
.dots span{width:11px;height:11px;border-radius:50%;background:#e9c6a3}
.dots span.on{background:var(--orange)}
.product{position:absolute;top:482px;width:350px;height:185px}
.product-1{left:350px}.product-2{left:702px}
.product-img{position:absolute;left:0;top:0;width:130px;height:185px;background:linear-gradient(180deg,#eaf0e4,#2f74a8)}
.product-2 .product-img{background:linear-gradient(180deg,#eaf0e4,#6aa33a)}
.product-title{position:absolute;left:145px;top:0;font-size:17px;color:var(--orange)}
.product-text{position:absolute;left:145px;top:30px;width:198px;font-size:9.5px;line-height:13px}
.read-more{position:absolute;right:10px;bottom:0;background:var(--green-mid);color:var(--white);font-size:13px;padding:6px 12px;border-radius:3px}
.footer{position:absolute;left:0;top:680px;width:1200px;height:52px;background:var(--green-dark);color:var(--white);font-size:11px}
.footer-brand{position:absolute;left:140px;top:18px;font-family:"Lato",sans-serif;font-weight:900;font-size:15px;color:var(--orange-light)}
.copy{position:absolute;left:235px;top:12px;line-height:14px}
.footer-nav{position:absolute;left:470px;top:18px;display:flex}
.footer-nav a{color:var(--white);text-decoration:none;padding:0 22px;border-right:1px solid #5b7a48}
.footer-nav a:last-child{border-right:0}
.social{position:absolute;left:968px;top:12px;display:flex;gap:10px}
.social span{width:26px;height:26px;border-radius:50%;background:#9aa893}
</style>
</head>
<body>
<header class="header">
  <div class="brand"><span class="brand-mark"></span><span class="brand-name">Lumavextra</span></div>
  <div class="tagline">PRODUCTS TO MAXIMIZE LIFE</div>
  <div class="search">
    <div class="search-icon"><svg width="20" height="20" viewBox="0 0 20 20"><circle cx="8" cy="8" r="6" fill="none" stroke="#fff" stroke-width="2.5"/><line x1="12.5" y1="12.5" x2="18" y2="18" stroke="#fff" stroke-width="3"/></svg></div>
    <div class="search-field">enter your search</div>
    <div class="search-btn">search</div>
  </div>
  <nav class="nav">
    <a class="active">Products</a><a>About Us</a><a>Contact Us</a><a>Our Purpose</a><a>Lumavextra FAQ's</a><a>Blog</a>
  </nav>
</header>

<aside>
  <section class="box videos">
    <div class="box-title">SOME VIDEOS</div>
    <div class="video-thumb" role="img" aria-label="Video thumbnail">
      <svg width="50" height="50" viewBox="0 0 50 50"><circle cx="25" cy="25" r="23" fill="rgba(255,255,255,.6)"/><path d="M19 14 L37 25 L19 36Z" fill="#5a7fa0"/></svg>
    </div>
  </section>
  <section class="box categories">
    <div class="box-title">Categories</div>
    <ul><li>Category 1</li><li>Category 2</li><li>Category 3</li></ul>
  </section>
  <section class="box user">
    <div class="box-title">User Panel</div>
    <div class="user-form">
      <div class="field">Username</div>
      <div class="field">Password</div>
      <div class="actions"><span class="btn-small">sign up</span><span class="btn-small">sign in</span></div>
      <div class="forgot">Forgot Password</div>
    </div>
  </section>
</aside>

<main>
  <div class="slider">
    <div class="slide-art" role="img" aria-label="The word vitamin spelled out with fresh vegetables"></div>
    <div class="dots"><span class="on"></span><span></span><span></span><span></span><span></span></div>
  </div>

  <article class="product product-1">
    <div class="product-img" role="img" aria-label="Mega Potency Fish Oil product box"></div>
    <h3 class="product-title">Mega Potency Fish Oil</h3>
    <p class="product-text">Our Mega Potency Fish Oil is rich in two essential fatty acids (more commonly known as EFAs) essential to human health are omega-3 and omega-6. By far, the best type of omega-3 fat is found in fish. The omega-3 in fish is high</p>
    <span class="read-more">Read More</span>
  </article>
  <article class="product product-2">
    <div class="product-img" role="img" aria-label="Organic Fruits and Greens Blend product box"></div>
    <h3 class="product-title">Mega Potency Fish Oil</h3>
    <p class="product-text">Our Mega Potency Fish Oil is rich in two essential fatty acids (more commonly known as EFAs) essential to human health are omega-3 and omega-6. By far, the best type of omega-3 fat is found in fish. The omega-3 in fish is high</p>
    <span class="read-more">Read More</span>
  </article>
</main>

<footer class="footer">
  <div class="footer-brand">Lumavextra</div>
  <div class="copy">Copyright 2012<br>http://lumavextra.com</div>
  <nav class="footer-nav"><a>Home</a><a>Shipping and Returns</a><a>Privacy Notice</a><a>Site Map</a></nav>
  <div class="social"><span></span><span></span><span></span><span></span></div>
</footer>
</body>
</html>
```